Verdo Consultants Exhibition Booth Design. Cannabis Legal Consultancy

We require a design for the following artwork in PDF of Jpeg high resolution format with these specifications, a 5cm bleed outside and a 10cm safe inside bleed. A tension fabric backdrop 200cm wide and 231cm high. (example loaded) Please see our website www.theverdoconsultants.co.uk
Attached are company logos and head shots for inclusion. You will see our colour schemes from the website. It should announce who we are and provide the company website.

```html
<!DOCTYPE html>
<html lang="en">
<head>
<meta charset="utf-8">
<title>Verdo Consultants – Who We Are</title>
<link rel="stylesheet" href="https://fonts.googleapis.com/css2?family=Montserrat:wght@400;500;700;800&family=Figtree:wght@400&display=swap">
<style>
  :root {
    --page: #f2f3f4;
    --navy-deep: #0a121a;
    --navy: #13202a;
    --teal-shade: #2c4248;
    --white: #ffffff;
    --blue: #1560b4;
    --line-blue: #4b8fb6;
    --photo-light: #d6d8da;
    --photo-mid: #9da2a8;
  }
  * { margin: 0; padding: 0; box-sizing: border-box; }
  html, body {
    width: 1157px; height: 1200px; overflow: hidden;
    background: var(--page);
  }
  .backdrop {
    position: absolute; left: 76px; top: 20px;
    width: 1095px; height: 1265px;
    transform: scale(0.917); transform-origin: 0 0;
    overflow: hidden; color: var(--white);
  }
  .backdrop__scene {
    position: absolute; inset: 0;
    background:
      radial-gradient(ellipse 55% 45% at 88% 55%, rgba(88,120,126,.55), transparent 70%),
      radial-gradient(ellipse 40% 35% at 20% 55%, rgba(50,72,80,.35), transparent 70%),
      linear-gradient(160deg, var(--navy-deep) 0%, var(--navy) 55%, var(--teal-shade) 100%);
  }
  .frame-line { position: absolute; }
  .frame-line--left { left: 35px; top: 83px; width: 2px; height: 1130px; background: rgba(75,143,182,.55); }
  .frame-line--bottom { left: 35px; top: 1213px; width: 867px; height: 2px; background: rgba(75,143,182,.55); }
  .frame-line--right { left: 1059px; top: 243px; width: 3px; height: 905px; background: var(--line-blue); }

  .brand { position: absolute; left: 102px; top: 74px; }
  .brand__name {
    font-family: "Montserrat", sans-serif; font-weight: 500;
    font-size: 30px; line-height: 34px; letter-spacing: .3px;
  }
  .brand__url { font-family: "Montserrat", sans-serif; font-weight: 500; font-size: 13px; margin-top: 6px; letter-spacing: .2px; }

  .portraits { position: absolute; left: 0; top: 0; width: 1095px; height: 600px; }

  .headline {
    position: absolute; left: 101px; top: 596px;
    font-family: "Montserrat", sans-serif; font-weight: 800;
    font-size: 96px; line-height: 110px; letter-spacing: -1px;
  }
  .headline-rule { position: absolute; left: 103px; top: 718px; width: 496px; height: 2px; background: var(--white); }

  .intro {
    position: absolute; left: 103px; top: 747px; width: 893px;
    font-family: "Figtree", sans-serif; font-size: 30px; line-height: 39.7px;
    letter-spacing: 1.2px;
    text-align: justify; text-align-last: left;
  }
  .site-link {
    position: absolute; left: 102px; top: 1143px;
    font-family: "Montserrat", sans-serif; font-weight: 700; font-size: 31px;
  }
</style>
</head>
<body>
  <div class="backdrop">
    <div class="backdrop__scene" role="img" aria-label="Dark blue-toned photograph of cannabis leaves filling the background"></div>
    <div class="frame-line frame-line--left"></div>
    <div class="frame-line frame-line--bottom"></div>
    <div class="frame-line frame-line--right"></div>

    <div class="brand">
      <div class="brand__name">Verdo Consultants</div>
      <div class="brand__url">www.theverdoconsultants.co.uk</div>
    </div>

    <svg class="portraits" viewBox="0 0 1095 600">
      <defs>
        <linearGradient id="photoTone" x1="0" y1="0" x2="0" y2="1">
          <stop offset="0" stop-color="#d6d8da"/>
          <stop offset="0.55" stop-color="#9da2a8"/>
          <stop offset="1" stop-color="#1b2633"/>
        </linearGradient>
      </defs>
      <g role="img" aria-label="Head-and-shoulders portrait of a consultant in a dark blazer and light shirt">
        <polygon points="645,190 735,11 955,11 1053,190 955,366 735,366" fill="url(#photoTone)" stroke="#ffffff" stroke-width="5"/>
      </g>
      <g role="img" aria-label="Portrait of a bearded consultant in glasses and a pinstripe suit">
        <polygon points="315,380 415,203 625,203 725,380 625,558 415,558" fill="url(#photoTone)" stroke="#ffffff" stroke-width="5"/>
      </g>
      <polygon points="539,134 567,85 627,85 655,134 627,183 567,183" fill="#1560b4" stroke="#ffffff" stroke-width="4"/>
      <polygon points="713,440 741,391 801,391 829,440 801,489 741,489" fill="#1560b4" stroke="#ffffff" stroke-width="4"/>
    </svg>

    <h1 class="headline">WHO WE ARE</h1>
    <div class="headline-rule"></div>

    <p class="intro">We can undertake and facilitate a top to bottom, seed to shelf, inception to sale assessment of your whole enterprise. We can facilitate a written expert legal opinion as to the compliance of your business and provide guidance on your structure and protection. We can assist you with the implementation of any necessary steps to achieve compliance, including the introduction to our cross-business contacts to make you stronger and more effective in the marketplace.</p>

    <div class="site-link">www.theverdoconsultants.co.uk</div>
  </div>
</body>
</html>
```